Falcrest security business card

Looking for a business card for my security company

Target Market(s)

Security

Industry/Entity Type

Security

Contact Information for Business Card

Name - Gil Marston. Title - General manager - direct 314 862.4490 website www. falcrestsecurityservices.example email - gil@ falcrestsecurityservices.example

Requirements
Must have
• Logo attached

```html
<!DOCTYPE html>
<html lang="en">
<head>
<meta charset="utf-8">
<title>Falcrest Security Services – Business Card</title>
<link rel="stylesheet" href="https://fonts.googleapis.com/css2?family=Open+Sans:wght@400;600;800&display=swap">
<style>
  :root {
    --page-bg: #121212;
    --card-bg: #1c1c1c;
    --card-bg-edge: #151515;
    --gold: #c9a45c;
    --gold-deep: #a47f3a;
    --text-light: #f2f2f2;
    --icon-ink: #1c1c1c;
  }
  * { margin: 0; padding: 0; box-sizing: border-box; }
  html, body {
    width: 1200px;
    height: 900px;
    overflow: hidden;
    background: var(--page-bg);
    font-family: "Open Sans", Arial, sans-serif;
  }
  .stage {
    width: 1200px;
    height: 900px;
    display: flex;
    align-items: center;
    justify-content: center;
  }
  .business-card {
    position: relative;
    width: 1000px;
    height: 572px;
    background: radial-gradient(ellipse at 50% 45%, var(--card-bg) 0%, var(--card-bg-edge) 100%);
    box-shadow: 0 20px 50px rgba(0,0,0,0.6);
    display: flex;
    align-items: center;
  }
  .brand {
    width: 460px;
    display: flex;
    justify-content: center;
    align-items: center;
  }
  .brand-name {
    font-weight: 800;
    font-size: 78px;
    letter-spacing: 2px;
    text-transform: uppercase;
    color: var(--gold);
  }
  .divider {
    width: 2px;
    height: 250px;
    background: var(--gold-deep);
  }
  .contact-block {
    padding-left: 50px;
  }
  .person-name {
    font-weight: 800;
    font-size: 38px;
    text-transform: uppercase;
    color: var(--gold);
    line-height: 1.1;
  }
  .person-title {
    font-size: 24px;
    color: var(--text-light);
    margin-top: 4px;
  }
  .contact-list {
    list-style: none;
    margin-top: 34px;
  }
  .contact-item {
    display: flex;
    align-items: center;
    gap: 14px;
    font-size: 23px;
    color: var(--text-light);
    line-height: 1.45;
  }
  .contact-icon {
    width: 22px;
    height: 22px;
    flex: none;
  }
</style>
</head>
<body>
<main class="stage">
  <section class="business-card">
    <div class="brand">
      <span class="brand-name">Falcrest</span>
    </div>
    <div class="divider"></div>
    <div class="contact-block">
      <h1 class="person-name">Gil Marston</h1>
      <p class="person-title">General manager</p>
      <ul class="contact-list">
        <li class="contact-item">
          <svg class="contact-icon" viewBox="0 0 22 22" aria-hidden="true">
            <circle cx="11" cy="11" r="11" fill="var(--gold)"/>
            <path d="M7 6.5c.8-.6 1.5-.4 1.9.3l.8 1.5c.3.6.1 1.1-.4 1.5l-.5.4c.6 1.3 1.5 2.2 2.8 2.8l.4-.5c.4-.5.9-.7 1.5-.4l1.5.8c.7.4.9 1.1.3 1.9-.8 1-2 1.3-3.2.7-2.4-1.2-4.1-2.9-5.3-5.3-.6-1.2-.3-2.4.7-3.2z" fill="var(--icon-ink)"/>
          </svg>
          <span>314 862.4490</span>
        </li>
        <li class="contact-item">
          <svg class="contact-icon" viewBox="0 0 22 22" aria-hidden="true">
            <circle cx="11" cy="11" r="11" fill="var(--gold)"/>
            <rect x="5.5" y="7" width="11" height="8" fill="none" stroke="var(--icon-ink)" stroke-width="1.4"/>
            <path d="M5.5 7l5.5 4.5L16.5 7" fill="none" stroke="var(--icon-ink)" stroke-width="1.4"/>
          </svg>
          <span>gil@falcrestsecurityservices.example</span>
        </li>
        <li class="contact-item">
          <svg class="contact-icon" viewBox="0 0 22 22" aria-hidden="true">
            <circle cx="11" cy="11" r="11" fill="var(--gold)"/>
            <circle cx="11" cy="11" r="5.5" fill="none" stroke="var(--icon-ink)" stroke-width="1.3"/>
            <ellipse cx="11" cy="11" rx="2.3" ry="5.5" fill="none" stroke="var(--icon-ink)" stroke-width="1.1"/>
            <path d="M5.5 11h11" stroke="var(--icon-ink)" stroke-width="1.1"/>
          </svg>
          <span>falcrestsecurityservices.example</span>
        </li>
      </ul>
    </div>
  </section>
</main>
</body>
</html>
```